Bookmarks for teachers and high school students - Range of 6

We are after a range of 6 bookmarks to use as hand outs to schools and students that we supply books and other school resources to.

Each bookmark is to have an inspirational quote on it and be a different color. You can decide color and background texture.

The back of them shall all be black or white, so just fronts needed. We want these 6 bookmarks to be similar in design, so they look like a matching range. And be nice enough that teachers and students will pick one to use.

We also want our logo to be on the bookmark, maybe just tucked down the bottom and our web address showing please - www.tarleby.com.au

Attached is the 6 quotes we want to use and an examples of the type of font I would like to see. But each a different font ..Also attached is our logo.

I think simple and smart may be best, but see what you come up with as I am also open to making them funky for students (if possible)

The print size of each bookmark is 40mm by 210mm

Target Market(s)

teachers and high school students

Industry/Entity Type

School

Requirements
Must have
• be eye catching

```html
<!DOCTYPE html>
<html lang="en">
<head>
<meta charset="utf-8">
<title>Tarleby Bookmark Range</title>
<link rel="stylesheet" href="https://fonts.googleapis.com/css2?family=Alegreya+Sans:ital,wght@1,400&family=Pridi:wght@600&family=Saira+Condensed:wght@700&family=Graduate&family=Julius+Sans+One&family=Libre+Baskerville:wght@700&family=Montserrat:wght@400;500&display=swap">
<style>
  :root {
    --page: #f1ece5;
    --card: #ffffff;
    --ink: #1d1d1d;
    --hole: #c9a57c;
    --accent-red: #d4261c;
    --bloom-green: #8fd27a;
    --bloom-pink: #f09ab4;
    --bloom-violet: #a98bd8;
    --blossom-pink: #f4a3b8;
    --blossom-brown: #a0725a;
    --band-teal: #3aa9a0;
    --band-orange: #f08a4b;
    --band-navy: #2e3a4f;
    --band-yellow: #f0e23a;
    --band-red: #e44a3c;
    --band-black: #222222;
    --band-pink: #ef6aa0;
    --band-lime: #9bdc6a;
    --band-sky: #5ec3e6;
  }
  * { box-sizing: border-box; margin: 0; padding: 0; }
  html, body { width: 1200px; height: 900px; overflow: hidden; }
  body { background: var(--page); position: relative; font-family: "Montserrat", sans-serif; color: var(--ink); }

  .bookmark {
    position: absolute; width: 566px; height: 112px;
    background: var(--card); border-radius: 5px;
    box-shadow: 0 2px 5px rgba(0,0,0,.18);
    overflow: hidden;
  }
  .bookmark--magic   { left: 20px;  top: 142px; }
  .bookmark--dreams  { left: 20px;  top: 300px; }
  .bookmark--tree    { left: 20px;  top: 472px; }
  .bookmark--logic   { left: 602px; top: 300px; }
  .bookmark--plan    { left: 602px; top: 472px; }
  .bookmark--together{ left: 602px; top: 645px; }

  .punch-hole {
    position: absolute; left: 14px; top: 46px; width: 20px; height: 20px;
    border-radius: 50%; background: var(--hole);
    box-shadow: inset 0 1px 2px rgba(0,0,0,.35);
  }

  .floral { position: absolute; top: 0; height: 112px; width: 110px; border-radius: 40px; }
  .floral--left { left: 52px; }
  .floral--right { left: 440px; }
  .floral--meadow { background: radial-gradient(ellipse at 50% 55%, var(--bloom-pink) 0%, var(--bloom-violet) 28%, var(--bloom-green) 55%, rgba(255,255,255,0) 75%); opacity: .75; }
  .floral--blossom { background: radial-gradient(ellipse at 50% 50%, var(--blossom-pink) 0%, #f7c2cf 35%, var(--blossom-brown) 60%, rgba(255,255,255,0) 76%); opacity: .7; }

  .bands { position: absolute; inset: 0; width: 566px; height: 112px; }

  .copy {
    position: absolute; top: 8px; left: 150px; width: 300px; height: 96px;
    display: flex; flex-direction: column; align-items: center; text-align: center;
  }
  .quote { line-height: 1.08; }
  .credit { font-family: "Montserrat", sans-serif; font-size: 10.5px; letter-spacing: 1px; text-transform: uppercase; margin-top: 3px; }
  .signoff {
    position: absolute; bottom: 9px; left: 0; right: 0;
    display: flex; align-items: center; justify-content: center; gap: 7px;
    font-family: "Montserrat", sans-serif; font-size: 10.5px; letter-spacing: .3px;
  }
  .brand-name { font-family: "Montserrat", sans-serif; font-weight: 500; font-size: 12.5px; letter-spacing: 1.5px; }
  .signoff-dot { width: 5px; height: 5px; border-radius: 50%; background: var(--ink); }

  .quote--magic { font-family: "Alegreya Sans", sans-serif; font-style: italic; font-size: 24px; }
  .quote--dreams { font-family: "Pridi", serif; font-weight: 600; font-size: 20px; }
  .quote--tree { font-family: "Saira Condensed", sans-serif; font-weight: 700; font-style: italic; font-size: 17px; text-transform: uppercase; line-height: 1; }
  .quote--logic { font-family: "Graduate", serif; font-size: 16px; line-height: 1.1; }
  .quote--plan { font-family: "Julius Sans One", sans-serif; font-size: 17px; line-height: 1.15; }
  .quote--together { font-family: "Libre Baskerville", serif; font-weight: 700; font-size: 14.5px; line-height: 1.2; }
  .copy--wide { left: 120px; width: 326px; }
</style>
</head>
<body>

<article class="bookmark bookmark--magic">
  <span class="punch-hole"></span>
  <div class="floral floral--left floral--meadow" role="img" aria-label="Painted sprig of wildflowers in pink, violet and green"></div>
  <div class="floral floral--right floral--meadow" role="img" aria-label="Painted sprig of wildflowers in pink, violet and green"></div>
  <div class="copy">
    <p class="quote quote--magic">“Those that don’t believe in magic,<br>will never find it.”</p>
    <p class="credit">-Rowan Dell</p>
  </div>
  <footer class="signoff"><span class="brand-name">TARLEBY</span><span class="signoff-dot"></span><span>www.tarleby.com.au</span></footer>
</article>

<article class="bookmark bookmark--dreams">
  <span class="punch-hole"></span>
  <div class="floral floral--left floral--meadow" role="img" aria-label="Painted bouquet of pink and blue flowers with green stems"></div>
  <div class="floral floral--right floral--meadow" role="img" aria-label="Painted bouquet of pink and blue flowers with green stems"></div>
  <div class="copy copy--wide">
    <p class="quote quote--dreams">“Dreams can come true, if we have<br>the courage to pursue them.”</p>
    <p class="credit">-Wes Darnley</p>
  </div>
  <footer class="signoff"><span class="brand-name">TARLEBY</span><span class="signoff-dot"></span><span>www.tarleby.com.au</span></footer>
</article>

<article class="bookmark bookmark--tree">
  <span class="punch-hole"></span>
  <div class="floral floral--left floral--blossom" role="img" aria-label="Painted cherry blossom branch"></div>
  <div class="floral floral--right floral--blossom" role="img" aria-label="Painted cherry blossom branch"></div>
  <div class="copy">
    <p class="quote quote--tree">“The best time to plant a tree was<br>20 years ago. The second best time<br>is now.”</p>
    <p class="credit">-Chinese Proverb</p>
  </div>
  <footer class="signoff"><span class="brand-name">TARLEBY</span><span class="signoff-dot"></span><span>www.tarleby.com.au</span></footer>
</article>

<article class="bookmark bookmark--logic">
  <span class="punch-hole"></span>
  <svg class="bands" viewBox="0 0 566 112" role="img" aria-label="Curved bands of folk pattern in teal, orange and navy">
    <defs><linearGradient id="logic-band" x1="0" x2="1"><stop offset="0" stop-color="var(--band-teal)"/><stop offset=".5" stop-color="var(--band-orange)"/><stop offset="1" stop-color="var(--band-navy)"/></linearGradient></defs>
    <path d="M72 0 L122 0 Q92 56 112 112 L62 112 Q44 56 72 0 Z" fill="url(#logic-band)"/>
    <path d="M500 0 L450 0 Q478 56 458 112 L508 112 Q526 56 500 0 Z" fill="url(#logic-band)"/>
  </svg>
  <div class="copy">
    <p class="quote quote--logic">“Logic will get you from A-Z,<br>imagination will get you<br>everywhere.”</p>
    <p class="credit">-Alder Ebbington</p>
  </div>
  <footer class="signoff"><span class="brand-name">TARLEBY</span><span class="signoff-dot"></span><span>www.tarleby.com.au</span></footer>
</article>

<article class="bookmark bookmark--plan">
  <span class="punch-hole"></span>
  <svg class="bands" viewBox="0 0 566 112" role="img" aria-label="Curved bands of folk pattern in black, yellow and red">
    <defs><linearGradient id="plan-band" x1="0" x2="1"><stop offset="0" stop-color="var(--band-black)"/><stop offset=".4" stop-color="var(--band-yellow)"/><stop offset=".7" stop-color="var(--band-red)"/><stop offset="1" stop-color="var(--band-black)"/></linearGradient></defs>
    <path d="M60 0 L112 0 Q86 56 104 112 L52 112 Q36 56 60 0 Z" fill="url(#plan-band)"/>
    <path d="M510 0 L460 0 Q486 56 466 112 L516 112 Q532 56 510 0 Z" fill="url(#plan-band)"/>
  </svg>
  <div class="copy copy--wide">
    <p class="quote quote--plan">“It doesn’t matter who we are,<br>what matters is our plan.”</p>
    <p class="credit">-The Night Warden Returns</p>
  </div>
  <footer class="signoff"><span class="brand-name">TARLEBY</span><span class="signoff-dot"></span><span>www.tarleby.com.au</span></footer>
</article>

<article class="bookmark bookmark--together">
  <span class="punch-hole"></span>
  <svg class="bands" viewBox="0 0 566 112" role="img" aria-label="Curved bands of folk pattern in pink, lime and sky blue">
    <defs><linearGradient id="together-band" x1="0" x2="1"><stop offset="0" stop-color="var(--band-pink)"/><stop offset=".5" stop-color="var(--band-lime)"/><stop offset="1" stop-color="var(--band-sky)"/></linearGradient></defs>
    <path d="M62 0 L116 0 Q90 56 108 112 L56 112 Q40 56 62 0 Z" fill="url(#together-band)"/>
    <path d="M506 0 L456 0 Q482 56 462 112 L512 112 Q528 56 506 0 Z" fill="url(#together-band)"/>
  </svg>
  <div class="copy copy--wide">
    <p class="quote quote--together">“Coming together is a beginning;<br>keeping together is a progress;<br>working together is success.”</p>
    <p class="credit">-Harlan Forde</p>
  </div>
  <footer class="signoff"><span class="brand-name">TARLEBY</span><span class="signoff-dot"></span><span>www.tarleby.com.au</span></footer>
</article>

</body>
</html>
```